Kestrel Homes Australia Business Card

We need a Business Card design for our new start up company.
A unique model designed to address Australia’s growing housing affordability problem has been launched. More than half of Australians are being priced out of the property market and have resigned themselves to the fact that they may never be able to afford a home.
We have developed a unique Algorithm that allows people to get into property and reverse this trend of domination by the property investors in this country. The first of its kind model facilitates connecting people to lending facilities that do not require them to have the finance combined under the purchase contract.
Ownership is shared with a second-tier investor, made up of either family or friends if not, Kestrel Homes Australia will provide a mini property investor enabling thousands of people the opportunity to buy a home, which they otherwise thought was not possible.
Kestrel Homes Australia is addressing housing affordability for families and individuals, giving every Australian looking to buy a home the opportunity to enter the property market to live in or invest.
Under our unique model, there is no combined finance, and individuals are assessed for their percentage portion of the property only. “A unique feature of our product is it is based around the strategies used for property investment. I have developed a unique Algorithm that enables the Home buyer to purchase 60% of a property, while Kestrel Homes Australia facilitates a second-tier investor to buy the other 40%. The Algorithm locks the investor in place and enables the home buyer to stairway to full ownership. The investment is secured against real property.
Please refer to our website www.kestrelhomes.com.au for inspiration.
Also please find attached our logo.
Any further directions please ask.
Cheers Marcus
Industry/Entity Type
Real Estate
Contact Information for Business Card
Marcus Thorley
CEO
Mobile 0400 615 272
www.kestrelhomes.com.au
Email: marcus@kestrelhomes.com.au
Colors
Designer to choose colors to be used in the design.
Look and feel

```html
<!DOCTYPE html>
<html lang="en">
<head>
<meta charset="utf-8">
<title>Kestrel Homes Australia — Business Card</title>
<link rel="stylesheet" href="https://fonts.googleapis.com/css2?family=Montserrat:wght@500;600;700&family=Roboto+Condensed:wght@400;500&family=Roboto:wght@400&display=swap">
<style>
  :root {
    --stage: #2a2a2a;
    --paper: #f3f3f3;
    --teal: #0aa4c8;
    --green: #3d8f1f;
    --ink: #4a4a4a;
    --faint: #d6e9f2;
    --white: #ffffff;
  }
  * { margin: 0; padding: 0; box-sizing: border-box; }
  html, body { width: 1200px; height: 960px; overflow: hidden; }
  body { background: var(--stage); position: relative; font-family: "Roboto", Arial, sans-serif; }

  .card { position: absolute; width: 600px; height: 343px; overflow: hidden; }
  .card--front { left: 314px; top: 113px; background: var(--paper); }
  .card--back { left: 311px; top: 472px; background: var(--teal); color: var(--white); text-align: center; }

  .front__artwork {
    position: absolute; right: 0; top: 0; width: 310px; height: 343px;
    background: linear-gradient(100deg, rgba(214,233,242,0) 0%, var(--faint) 45%, var(--faint) 100%);
    opacity: .8;
  }

  .brand { position: absolute; left: 55px; top: 100px; }
  .brand__name {
    font-family: "Montserrat", Arial, sans-serif; font-weight: 700;
    font-size: 19px; color: var(--teal); white-space: nowrap;
  }
  .brand__dot {
    display: inline-block; width: 10px; height: 10px; border-radius: 50%;
    background: var(--teal); margin-left: 4px; vertical-align: 2px;
  }
  .brand__tagline {
    font-family: "Montserrat", Arial, sans-serif; font-weight: 600;
    font-size: 11.5px; color: var(--green); margin: 4px 0 0 20px; white-space: nowrap;
  }

  .accent-bar { position: absolute; left: 0; top: 178px; width: 13px; height: 41px; background: var(--teal); }

  .person { position: absolute; left: 55px; top: 176px; }
  .person__name {
    font-family: "Roboto Condensed", Arial, sans-serif; font-weight: 500;
    font-size: 22px; color: var(--teal); text-transform: uppercase; line-height: 1.1;
  }
  .person__role {
    font-family: "Roboto Condensed", Arial, sans-serif; font-weight: 400;
    font-size: 16px; color: var(--green); margin-top: 3px;
  }

  .contacts { position: absolute; left: 55px; top: 243px; list-style: none; }
  .contacts li {
    display: flex; align-items: center; height: 19.5px;
    font-size: 14px; color: var(--ink);
  }
  .contacts svg { width: 14px; height: 14px; margin-right: 7px; flex: none; }

  .back__brand { position: absolute; left: 0; right: 0; top: 180px; }
  .back__name {
    font-family: "Montserrat", Arial, sans-serif; font-weight: 700; font-size: 28px;
  }
  .back__dot {
    display: inline-block; width: 12px; height: 12px; border-radius: 50%;
    background: var(--white); margin-left: 6px; vertical-align: 2px;
  }
  .back__tagline {
    font-family: "Montserrat", Arial, sans-serif; font-weight: 500; font-size: 16px; margin-top: 6px;
  }
  .back__url {
    position: absolute; left: 0; right: 0; top: 294px;
    font-size: 14px; letter-spacing: 8.9px; padding-left: 8.9px;
  }
</style>
</head>
<body>

<section class="card card--front">
  <div class="front__artwork" role="img" aria-label="Faint illustration of apartment towers and a house roofline"></div>

  <div class="brand">
    <div class="brand__name">Kestrel Homes Australia<span class="brand__dot"></span></div>
    <div class="brand__tagline">Opening Doors to Home Ownership</div>
  </div>

  <div class="accent-bar"></div>

  <div class="person">
    <div class="person__name">Marcus Thorley</div>
    <div class="person__role">CEO</div>
  </div>

  <ul class="contacts">
    <li>
      <svg viewBox="0 0 14 14" aria-hidden="true"><rect x="3" y="0.5" width="8" height="13" rx="1.5" fill="var(--teal)"/><rect x="4.5" y="2.5" width="5" height="8" fill="var(--white)"/></svg>
      0400615272
    </li>
    <li>
      <svg viewBox="0 0 14 14" aria-hidden="true"><rect x="0.5" y="3" width="13" height="9" fill="var(--teal)"/><path d="M1 3.5 L7 8 L13 3.5" fill="none" stroke="var(--white)" stroke-width="1.2"/></svg>
      marcus@kestrelhomes.com.au
    </li>
    <li>
      <svg viewBox="0 0 14 14" aria-hidden="true"><circle cx="7" cy="7" r="6.5" fill="var(--teal)"/><path d="M4 4 Q6 5 5 7 Q7 8 6 11 M9 3 Q8 5 10 6" fill="none" stroke="var(--white)" stroke-width="1.2"/></svg>
      www.kestrelhomes.com.au
    </li>
  </ul>
</section>

<section class="card card--back">
  <div class="back__brand">
    <div class="back__name">Kestrel Homes Australia<span class="back__dot"></span></div>
    <div class="back__tagline">Opening Doors to Home Ownership</div>
  </div>
  <div class="back__url">www.kestrelhomes.com.au</div>
</section>

</body>
</html>
```